| 希望する色 | 黄系 |
【 概要 】 PAKUのリッチの制作をお願いします。 ほぼデザインを出来ているのでデータへの落し込みと多少のブラッシュアップをお願い出来ればと思います。 【 依頼内容 】 添付した画像のように1枚の画像に6分割したリッチメニューになります。 ファイル形式:JPG、JPEG、PNG ファイルサイズ:1MB以下 画像サイズ:2500px × 1686px 【 提供素材 】 ・添付ファイルよりご確認下さい。 【 デザインイメージ 】 ・シンプル ・ピクトグラン ・こちらのサイトのPAKUアカウントで使用します https://morizuto.jp/ 良ければ友達追加をしてイメージ頂けますと幸いです。 <a href="https://tsu.ee/Q8pW2RZ"><img src="https://cdn.paku-assets.example/n/paku_add_friends/btn/ja.png" alt="友だち追加" height="36" border="0"></a> ご質問がありましたら、気軽にお問い合わせください。 応募をお待ちしております! |
| 参考記事URL | ||
| https://morizuto.jp/ | ||
どれも素敵なご提案を頂いたのですが一番動線を考えられた作品を選ばせて頂きました。
色々なご提案を頂いたのにお選び出来ずに申し訳ございません。
また色々と今後もお願いをする計画がございますのでぜひ次回もご参画を頂けますと幸いです。

```html
<!DOCTYPE html>
<html lang="ja">
<head>
<meta charset="utf-8">
<title>モリズト リッチメニュー</title>
<link rel="stylesheet" href="https://fonts.googleapis.com/css2?family=Noto+Sans+JP:wght@700&display=swap">
<style>
  :root {
    --frame: #f9cf4c;
    --tile-blue: #eef5fc;
    --tile-cream: #fefce8;
    --ink: #1f232e;
    --icon-blue: #7c9fd6;
    --icon-yellow: #fbcd4a;
    --white: #ffffff;
  }
  * { margin: 0; padding: 0; box-sizing: border-box; }
  html, body { width: 1200px; height: 808px; overflow: hidden; background: var(--frame); }
  .rich-menu {
    width: 1200px; height: 808px;
    padding: 16px;
    display: grid;
    grid-template-columns: repeat(3, 376px);
    grid-template-rows: repeat(2, 378px);
    gap: 20px;
  }
  .menu-tile {
    position: relative;
    border-radius: 22px;
    background: var(--tile-cream);
  }
  .menu-tile--blue { background: var(--tile-blue); }
  .menu-icon {
    position: absolute;
    left: 50%; top: 88px;
    width: 140px; height: 140px;
    transform: translateX(-50%);
  }
  .menu-icon--wide { width: 260px; top: 66px; height: 170px; }
  .operator-figure {
    position: absolute;
    left: 50%; top: 92px;
    width: 120px; height: 130px;
    transform: translateX(-50%);
    border-radius: 60px 60px 24px 24px;
    background: linear-gradient(180deg, var(--white) 0%, var(--icon-blue) 100%);
    border: 4px solid var(--ink);
  }
  .menu-label {
    position: absolute;
    left: 0; right: 0; top: 252px; height: 92px;
    display: flex; align-items: center; justify-content: center;
    text-align: center;
    font-family: "Noto Sans JP", sans-serif;
    font-weight: 700;
    font-size: 30px;
    line-height: 46px;
    letter-spacing: 0.12em;
    color: var(--ink);
  }
</style>
</head>
<body>
<main class="rich-menu">

  <section class="menu-tile menu-tile--blue">
    <div class="operator-figure" role="img" aria-label="ヘッドセットを着けたオペレーターのピクトグラム"></div>
    <p class="menu-label">モリズト</p>
  </section>

  <section class="menu-tile">
    <svg class="menu-icon" viewBox="0 0 120 120" aria-hidden="true">
      <g stroke="var(--ink)" stroke-width="4" stroke-linejoin="round" stroke-linecap="round">
        <rect x="10" y="18" width="100" height="92" rx="10" fill="var(--icon-yellow)"/>
        <line x1="10" y1="38" x2="110" y2="38"/>
        <line x1="34" y1="8" x2="34" y2="26"/>
        <line x1="86" y1="8" x2="86" y2="26"/>
        <g fill="var(--icon-yellow)" stroke-width="3.5">
          <rect x="46" y="48" width="12" height="12"/><rect x="64" y="48" width="12" height="12"/><rect x="82" y="48" width="12" height="12"/>
          <rect x="28" y="66" width="12" height="12"/><rect x="46" y="66" width="12" height="12"/>
          <rect x="28" y="84" width="12" height="12"/><rect x="46" y="84" width="12" height="12"/><rect x="64" y="84" width="12" height="12"/>
        </g>
        <polyline points="64,72 71,80 90,62" fill="none"/>
      </g>
    </svg>
    <p class="menu-label">内見予約</p>
  </section>

  <section class="menu-tile menu-tile--blue">
    <svg class="menu-icon" viewBox="0 0 120 120" aria-hidden="true">
      <g stroke="var(--ink)" stroke-width="4" stroke-linejoin="round" stroke-linecap="round">
        <rect x="14" y="10" width="80" height="100" rx="4" fill="var(--icon-blue)"/>
        <rect x="24" y="20" width="60" height="80" fill="var(--white)"/>
        <line x1="34" y1="36" x2="74" y2="36"/>
        <line x1="34" y1="50" x2="64" y2="50"/>
        <line x1="34" y1="64" x2="58" y2="64"/>
        <line x1="34" y1="78" x2="50" y2="78"/>
        <polygon points="100,24 112,36 74,74 58,80 64,64" fill="var(--icon-blue)"/>
        <line x1="64" y1="64" x2="74" y2="74"/>
      </g>
    </svg>
    <p class="menu-label">申込</p>
  </section>

  <section class="menu-tile">
    <svg class="menu-icon" viewBox="0 0 120 120" aria-hidden="true">
      <g stroke="var(--ink)" stroke-width="4" stroke-linejoin="round">
        <rect x="46" y="22" width="68" height="62" fill="var(--icon-yellow)"/>
        <path d="M46 44 H22 L8 66 V84 H46 Z" fill="var(--icon-yellow)"/>
        <path d="M22 50 H40 V64 H14 Z" fill="var(--white)"/>
        <line x1="8" y1="84" x2="114" y2="84"/>
        <circle cx="28" cy="90" r="11" fill="var(--white)"/>
        <circle cx="92" cy="90" r="11" fill="var(--white)"/>
      </g>
    </svg>
    <p class="menu-label">引越し業者<br>の手配</p>
  </section>

  <section class="menu-tile menu-tile--blue">
    <svg class="menu-icon menu-icon--wide" viewBox="0 0 260 170" aria-hidden="true">
      <g stroke="var(--ink)" stroke-width="3" fill="var(--icon-blue)">
        <circle cx="46" cy="40" r="34"/><circle cx="130" cy="40" r="34"/><circle cx="214" cy="40" r="34"/>
        <circle cx="88" cy="124" r="34"/><circle cx="172" cy="124" r="34"/>
      </g>
      <g stroke="var(--ink)" stroke-width="2.5" stroke-linejoin="round" stroke-linecap="round">
        <circle cx="46" cy="34" r="11" fill="var(--white)"/>
        <rect x="40" y="44" width="12" height="10" fill="var(--white)"/>
        <path d="M118 28 H142 V36 H134 V44 H118 Z" fill="var(--white)"/>
        <line x1="130" y1="20" x2="130" y2="28"/>
        <path d="M140 52 q3 6 0 10 q-3 -4 0 -10" fill="var(--white)"/>
        <path d="M198 52 H230 M202 52 q-4 -14 4 -22 q4 10 0 22 M214 52 q-4 -16 4 -24 q4 12 0 24 M226 52 q-4 -12 2 -20 q4 10 0 20" fill="var(--white)"/>
        <path d="M78 110 q-4 4 -2 10 q6 16 22 22 q6 2 10 -2 l-6 -8 l-8 3 q-8 -5 -12 -12 l4 -8 Z" fill="var(--white)"/>
        <circle cx="172" cy="124" r="16" fill="var(--white)"/>
        <ellipse cx="172" cy="124" rx="7" ry="16" fill="none"/>
        <line x1="156" y1="124" x2="188" y2="124"/>
      </g>
    </svg>
    <p class="menu-label">ライフライン<br>の手配</p>
  </section>

  <section class="menu-tile">
    <svg class="menu-icon" viewBox="0 0 120 120" aria-hidden="true">
      <g stroke="var(--ink)" stroke-width="4" stroke-linejoin="round">
        <path d="M52 58 L104 104 L96 112 L88 104 L82 108 L76 100 L70 104 L44 78 Z" fill="var(--icon-yellow)"/>
        <rect x="8" y="14" width="54" height="54" rx="14" transform="rotate(-40 35 41)" fill="var(--icon-yellow)"/>
        <rect x="24" y="32" width="22" height="8" rx="4" transform="rotate(-40 35 36)" fill="var(--white)"/>
      </g>
    </svg>
    <p class="menu-label">鍵受渡方法<br>を確認</p>
  </section>

</main>
</body>
</html>
```